For Tolvy: Business cards, letterhead, envelopes and double sided page

For Tolvy: Previously described in email.

Business cards, letterhead, envelopes, and glossy marketing double sided page.

Industry/Entity Type

Marketing

```html
<!DOCTYPE html>
<html lang="en">
<head>
<meta charset="utf-8">
<title>Tolvy envelope – front and back</title>
<link href="https://fonts.googleapis.com/css2?family=Arimo:wght@400;700&display=swap" rel="stylesheet">
<style>
  :root {
    --backdrop: #252a40;
    --paper: #ffffff;
    --edge: #1c1c22;
    --ink: #2a2f45;
    --muted: #8a96a6;
  }
  html, body {
    margin: 0;
    padding: 0;
    overflow: hidden;
  }
  .canvas {
    position: relative;
    width: 873px;
    height: 1200px;
    background: var(--backdrop);
    overflow: hidden;
    font-family: "Arimo", Arial, sans-serif;
  }
  .envelope-art {
    position: absolute;
    left: 0;
    top: 0;
    width: 873px;
    height: 1200px;
  }
  .envelope-art .sheet {
    fill: var(--paper);
    stroke: var(--edge);
    stroke-width: 3;
    stroke-linejoin: round;
  }
  .envelope-art .fold {
    stroke: var(--edge);
    stroke-width: 3;
    fill: none;
  }
  .brand {
    position: absolute;
    display: flex;
    align-items: center;
    color: var(--ink);
    font-weight: 700;
    letter-spacing: -0.5px;
  }
  .brand-mark {
    background: var(--ink);
    border-radius: 5px;
    flex: none;
  }
  .front-brand {
    left: 34px;
    top: 162px;
    font-size: 56px;
    gap: 12px;
    line-height: 1;
  }
  .front-brand .brand-mark {
    width: 76px;
    height: 50px;
  }
  .contact-icons {
    position: absolute;
    left: 38px;
    top: 223px;
    display: flex;
    flex-direction: column;
    gap: 9px;
  }
  .contact-icons span {
    display: block;
    width: 11px;
    height: 11px;
    border: 2px solid var(--ink);
    box-sizing: border-box;
    border-radius: 2px;
  }
  .back-brand {
    left: 0;
    width: 873px;
    top: 700px;
    justify-content: center;
    font-size: 30px;
    gap: 7px;
    line-height: 1;
  }
  .back-brand .brand-mark {
    width: 42px;
    height: 28px;
    border-radius: 3px;
  }
  .back-url {
    position: absolute;
    left: 0;
    width: 873px;
    top: 739px;
    text-align: center;
    color: var(--muted);
    font-size: 13px;
    letter-spacing: 1px;
  }
</style>
</head>
<body>
<main class="canvas">
  <svg class="envelope-art" viewBox="0 0 873 1200" aria-hidden="true">
    <!-- front envelope: open flap and body -->
    <polygon class="sheet" points="17,146 137,34 734,34 859,146"/>
    <rect class="sheet" x="17" y="146" width="842" height="416"/>
    <!-- back envelope: body, flap and folds -->
    <rect class="sheet" x="21" y="677" width="837" height="400"/>
    <line class="fold" x1="326" y1="779" x2="24" y2="1075"/>
    <line class="fold" x1="549" y1="779" x2="855" y2="1075"/>
    <polygon class="sheet" points="21,677 141,779 727,779 858,677"/>
  </svg>

  <div class="brand front-brand">
    <span class="brand-mark"></span>
    <span class="brand-name">Tolvy</span>
  </div>
  <div class="contact-icons">
    <span></span><span></span><span></span><span></span>
  </div>

  <div class="brand back-brand">
    <span class="brand-mark"></span>
    <span class="brand-name">Tolvy</span>
  </div>
  <div class="back-url">www.tolvy.com</div>
</main>
</body>
</html>
```